Tailmart.com Dog Coupon Site Website Design

FurSaver - Dog Coupon Site Design Brief

Project Overview
**Site Name:** TailMart.com
**Purpose:** A modern coupon aggregation platform specifically for dog and pet-related products and services
**Target Audience:** Dog owners, pet enthusiasts, budget-conscious pet parents

Brand Identity & Visual Direction

Typography
- **Headers:** Modern sans-serif (Inter or similar) - Clean and friendly
- **Body:** Readable sans-serif with good mobile legibility
- **Accent:** Playful but professional font for coupon codes

Design Principles
- **Flat Design:** Clean, minimal with subtle shadows
- **Friendly & Approachable:** Rounded corners, soft edges
- **Trust-Building:** Clear pricing, transparent savings
- **Scannable:** Easy-to-read coupon codes and offers

## User Experience & Functionality

### Homepage Features
1. **Hero Section**
- Clear value proposition
- Search functionality
- Featured savings highlight

2. **Coupon Cards**
- One-click copy functionality
- Clear discount display
- Store/brand logos
- Expiration dates
- "Get Deal" call-to-action

3. **Navigation**
- Categories (Food, Toys, Health, Services, etc.)
- Popular stores
- Latest deals

### Interactive Elements
- **Copy Button:** Instant feedback when coupon copied
- **Deal Pages:** Detailed offer information, terms, store details
- **Search & Filter:** By category, store, discount amount
- **Mobile Menu:** Hamburger navigation for mobile

## Technical Requirements

### Responsive Design
- **Mobile-First:** Optimized for touch interactions
- **Tablet:** Adapted layout for medium screens
- **Desktop:** Full-width utilization with sidebar potential

### Performance
- **Fast Loading:** Optimized images, minimal JavaScript
- **Accessibility:** WCAG compliant, screen reader friendly
- **SEO Optimized:** Structured data for deals and offers

## Content Strategy

### Deal Categories
- Dog Food & Treats
- Toys & Accessories
- Health & Grooming
- Training & Services
- Outdoor & Travel

### Key Messaging
- "Save on everything your dog loves"
- "Verified deals updated daily"
- "Your pup deserves the best for less"

## Conversion Optimization

### Trust Elements
- Deal verification badges
- User reviews/ratings
- Clear savings calculations
- Expiration date transparency

### Call-to-Actions
- "Copy Code" (primary action)
- "Get Deal" (secondary action)
- "View All [Store] Deals"

## Success Metrics
- Coupon copy rate
- Click-through to retailer
- User return visits
- Mobile vs desktop usage
- Category performance

This design brief ensures a user-friendly, trustworthy platform that makes finding and using pet deals effortless while maintaining a warm, dog-loving community feel.

1. Design Objective
Create a warm, energetic space where dog lovers instantly feel welcomed and confident they’re finding genuine savings for their furry friends. Everything from the layout to the smallest icon should reinforce trust, delight, and simplicity.
2. Visual Personality
Color Palette: Soft, cheerful hues—think warm yellows and gentle blues—that evoke sunshine and playfulness without overwhelming.
Typography:
Headings: A modern, friendly sans‑serif (like Inter) with open letterforms to feel approachable.
Body Copy: Highly legible sans‑serif with generous line spacing for comfort on small screens.
Accent Font: A slightly quirky, hand‑drawn style used sparingly for coupon codes and special call‑outs, giving a personal, “paw‑picked” touch.
Imagery & Icons: Real‑life photographs of happy dogs interspersed with clean line‑icons of bones, paw prints, and hearts. Rounded shapes and subtle shadows keep the look soft and contemporary.
3. Layout & Hierarchy
Hero Area:
Full‑bleed image of a joyful dog, overlaid with a single, punchy tagline (“Save on everything your dog loves”).
Prominent search bar centered to invite exploration.
Offer Grid:
Generous white space around each coupon card so the eye can rest and scan easily.
Coupon cards feature a bold discount label, brand logo, and a friendly “Get Deal” button.
A playful “Copied!” animation briefly replaces the button once the code is grabbed.
Navigation:
A fixed header with clear category labels (Food, Toys, Health, Services).
A secondary “Popular Stores” carousel below to spotlight key partners.
4. Interaction & Motion
Micro‑interactions:
Hover state for cards subtly lifts the card and deepens its shadow, inviting a click.
Copy‑code button pulses once on hover, hinting at its one‑click magic.
Transitions:
Smooth fades between deal filters and search results to reassure users that the site is responding.
Loading indicators shaped like spinning collars or wagging tails to keep the theme consistent.
5. Accessibility & Inclusivity
Ensure all text meets contrast standards so every pet parent—regardless of vision—can read offers with ease.
Interactive elements sized for easy tapping on touchscreens.
Alt‑text for all imagery describing dogs, products, and actions for screen‑reader users.
6. Emotional Tone
From the moment someone lands on TailMart.com, they should feel the joy of treating their dog without guilt. Friendly copy (“Your pup deserves the best for less”) paired with bright visuals will create a sense of community and shared passion.
7. Success by Design
Scan‑ability: Users should spot great deals in under two seconds.
Trust Signals: Badges (“Verified Savings”), clear expiration dates, and reviewer star icons should feel earned and prominent.
Return Visits: A “My Favorite Deals” heart icon encourages saving and returning, reinforced by subtle reminders in the UI.
This design approach keeps dog lovers front and center—making sure every graphic, font choice, and interaction feels like it was lovingly tailored for them.

Target Market(s)

Dog Lovers looking for good deals

Industry/Entity Type

Coupon Code

Number of Pages Required

4 page

Font styles to use
Sans Serif

Requirements
Must have
• Modern look, coupon copy cards it's a deal site and I want the coupon code and copy in the coupon card, blog section, review section, modern footer/header
Nice to have
• Modern coupon code website, easy to use

```html
<!DOCTYPE html>
<html lang="en">
<head>
<meta charset="utf-8">
<title>TailMart – Dog Deals</title>
<link href="https://fonts.googleapis.com/css2?family=Inter:wght@400;500;600;700&display=swap" rel="stylesheet">
<style>
:root{
  --blue:#3b82f6;
  --blue-dark:#2563eb;
  --green:#10b981;
  --ink:#111827;
  --text:#374151;
  --muted:#6b7280;
  --line:#e5e7eb;
  --soft:#f3f4f6;
  --pale:#f8fafc;
  --footer:#111827;
  --white:#ffffff;
}
*{box-sizing:border-box;margin:0;padding:0}
html,body{width:1200px;height:2962px;overflow:hidden}
body{font-family:'Inter',sans-serif;color:var(--text);background:var(--white)}
a{color:inherit;text-decoration:none}
.wrap{width:1000px;margin:0 auto}

.topbar{height:33px;background:var(--blue);color:#fff;font-size:12px;display:flex;align-items:center;justify-content:space-between;padding:0 27px}
.topbar .links{display:flex;gap:14px;font-weight:500}

.header{height:66px;display:flex;align-items:center;padding:0 27px;border-bottom:1px solid var(--line)}
.brand{display:flex;align-items:center;gap:8px;font-weight:700;font-size:21px;color:var(--ink);width:300px}
.brand .dot{width:22px;height:22px;border-radius:50%;background:var(--blue)}
.mainnav{display:flex;gap:28px;font-size:14px;color:var(--text);margin-left:35px;flex:1}
.searchbox{width:214px;height:34px;border:1px solid var(--line);border-radius:17px;display:flex;align-items:center;gap:8px;padding:0 13px;font-size:13px;color:#9ca3af}

.catnav{height:47px;background:var(--soft);display:flex;align-items:center;justify-content:space-between;padding:0 40px;font-size:14px;color:var(--text)}
.catnav span{display:flex;align-items:center;gap:8px}
.catnav svg{width:14px;height:14px;fill:var(--text)}

.hero{height:371px;position:relative;display:flex;flex-direction:column;align-items:center;color:#fff;text-align:center}
.hero .photo{position:absolute;inset:0;background:radial-gradient(ellipse at 50% 45%,#8a5a33 0%,#6b4a35 28%,#3f5e6e 55%,#2c4f66 100%)}
.hero .photo::after{content:"";position:absolute;inset:0;background:rgba(0,0,0,.28)}
.hero .inner{position:relative;padding-top:30px}
.hero h1{font-size:41px;line-height:41px;font-weight:700;width:600px}
.hero p{font-size:17px;margin-top:18px;font-weight:500}
.hero .bar{width:560px;height:50px;background:#fff;border-radius:25px;margin:23px auto 0;display:flex;align-items:center;justify-content:space-between;padding:0 4px 0 20px;font-size:15px;color:#9ca3af}
.hero .bar b{background:var(--blue);color:#fff;font-weight:500;font-size:13px;height:32px;width:85px;border-radius:16px;display:flex;align-items:center;justify-content:center}
.hero .chips{display:flex;gap:10px;justify-content:center;margin-top:21px}
.hero .chips span{background:rgba(255,255,255,.25);border-radius:12px;padding:4px 13px;font-size:12px}

.section-title{font-size:25px;font-weight:700;color:var(--ink)}

.deals{height:455px;padding-top:54px}
.deal-grid{display:flex;gap:28px;margin-top:26px}
.deal{width:315px;height:291px;border:1px solid var(--line);border-radius:10px;padding:20px;position:relative;background:#fff;box-shadow:0 1px 3px rgba(0,0,0,.04)}
.deal .store{width:100px;height:34px;background:var(--soft);display:flex;align-items:center;justify-content:center;font-size:13px;font-weight:600;color:var(--ink);gap:5px}
.deal .store i{width:10px;height:10px;border-radius:50%;background:#f59e0b;display:block}
.deal .heart{position:absolute;right:20px;top:20px;width:22px;height:22px}
.deal .off{display:inline-block;margin-top:14px;background:var(--blue);color:#fff;font-weight:600;font-size:17px;padding:7px 14px;border-radius:5px}
.deal p{font-size:13.5px;line-height:20px;margin-top:15px;color:var(--text)}
.deal .exp{font-size:12px;color:var(--muted);margin-top:11px;display:flex;gap:6px;align-items:center}
.deal .copy{margin-top:12px;height:40px;background:var(--green);color:#fff;border-radius:5px;font-weight:500;font-size:14px;display:flex;align-items:center;justify-content:center}
.deal .ver{margin-top:16px;font-size:12px;display:flex;gap:6px;align-items:center}

.cats{height:504px;background:var(--soft);padding-top:52px}
.cats .wrap{width:946px}
.cat-grid{display:grid;grid-template-columns:repeat(3,302px);gap:20px;margin-top:26px}
.cat{height:160px;border-radius:6px;position:relative;overflow:hidden;color:#fff;display:flex;flex-direction:column;align-items:center;justify-content:center;text-align:center}
.cat::after{content:"";position:absolute;inset:0;background:rgba(0,0,0,.3)}
.cat>*{position:relative;z-index:1}
.cat svg{width:26px;height:26px;fill:#fff}
.cat b{font-size:17px;font-weight:600;margin-top:4px}
.cat small{font-size:13px;margin-top:6px;opacity:.9}

.stores{height:219px;padding-top:41px}
.store-row{display:flex;margin-top:25px}
.store-row div{width:194px;height:74px;display:flex;align-items:center;justify-content:center;font-size:24px;font-weight:700;color:var(--ink)}

.tips{height:519px;background:var(--pale);padding-top:54px}
.tip-grid{display:flex;gap:28px;margin-top:26px}
.tip{width:315px;height:353px;background:#fff;border:1px solid var(--line);border-radius:8px;overflow:hidden}
.tip .img{height:160px}
.tip .body{padding:20px}
.tip .tag{font-size:12px;color:var(--blue);font-weight:500}
.tip h3{font-size:17px;line-height:23px;font-weight:600;color:var(--ink);margin-top:10px}
.tip p{font-size:13.5px;line-height:20px;margin-top:12px}
.tip .read{font-size:12px;color:var(--muted);margin-top:12px;display:flex;gap:6px;align-items:center}

.trust{height:198px;display:flex;justify-content:center;padding-top:40px}
.trust div{width:257px;text-align:center}
.trust .ic{width:52px;height:52px;border-radius:50%;background:#e0ecfd;margin:0 auto;display:flex;align-items:center;justify-content:center}
.trust h4{font-size:16px;font-weight:600;color:var(--ink);margin-top:15px}
.trust p{font-size:13.5px;margin-top:10px;color:var(--text)}

.news{height:238px;background:var(--pale);text-align:center;padding-top:52px}
.news h2{font-size:25px;font-weight:700;color:var(--ink)}
.news p{font-size:14px;margin-top:14px}
.news form{display:flex;justify-content:center;gap:14px;margin-top:25px}
.news .in{width:428px;height:41px;border:1px solid var(--line);background:#fff;border-radius:5px;font-size:14px;color:#9ca3af;display:flex;align-items:center;padding:0 19px}
.news .btn{width:118px;height:41px;background:var(--blue);border-radius:5px;color:#fff;font-size:14px;font-weight:500;display:flex;align-items:center;justify-content:center}

.footer{height:312px;background:var(--footer);color:#9ca3af;padding-top:52px}
.foot-cols{display:flex;height:172px}
.foot-cols>div{width:257px}
.foot-brand{display:flex;align-items:center;gap:8px;color:#fff;font-weight:700;font-size:20px;margin-top:-4px}
.foot-brand i{width:20px;height:20px;border-radius:50%;background:var(--blue);display:block}
.foot-cols p{font-size:13.5px;line-height:20px;margin-top:18px;width:235px}
.foot-cols h5{color:#fff;font-size:14px;font-weight:600}
.foot-cols ul{list-style:none;margin-top:11px}
.foot-cols li{font-size:13.5px;line-height:27px}
.foot-bottom{border-top:1px solid #1f2937;display:flex;justify-content:space-between;align-items:center;height:86px;font-size:13.5px}
.social{display:flex;gap:14px}
.social span{width:33px;height:33px;border-radius:50%;background:#1f2937;display:block}
</style>
</head>
<body>

<div class="topbar"><span>Daily Updated Deals for Your Furry Friends</span><div class="links"><a href="#">Sign In</a><a href="#">Register</a></div></div>

<header class="header">
  <a class="brand" href="#"><span class="dot"></span>TailMart</a>
  <nav class="mainnav"><a>Home</a><a>About</a><a>Latest Deals</a><a>Services</a><a>Popular Stores</a><a>Blog</a></nav>
  <div class="searchbox"><svg width="13" height="13" viewBox="0 0 24 24" fill="none" stroke="#9ca3af" stroke-width="3"><circle cx="10" cy="10" r="7"/><path d="M15 15l6 6"/></svg>Search deals...</div>
</header>

<nav class="catnav">
  <span><svg viewBox="0 0 24 24"><circle cx="12" cy="15" r="6"/><circle cx="5" cy="8" r="2.5"/><circle cx="19" cy="8" r="2.5"/><circle cx="9" cy="4" r="2.5"/><circle cx="15" cy="4" r="2.5"/></svg>Dog Food</span>
  <span><svg viewBox="0 0 24 24"><path d="M2 2h10l10 10-10 10L2 12z"/></svg>Treats</span>
  <span><svg viewBox="0 0 24 24"><path d="M4 7h16v15H4z"/><path d="M8 7a4 4 0 018 0" fill="none" stroke="#374151" stroke-width="2"/></svg>Toys</span>
  <span><svg viewBox="0 0 24 24"><path d="M12 2l9 4v6c0 5-4 9-9 10-5-1-9-5-9-10V6z"/></svg>Health</span>
  <span><svg viewBox="0 0 24 24"><path d="M12 2c4 6 6 9 6 12a6 6 0 01-12 0c0-3 2-6 6-12z"/></svg>Grooming</span>
  <span><svg viewBox="0 0 24 24"><path d="M12 4l11 5-11 5L1 9z"/><path d="M6 12v5c3 3 9 3 12 0v-5l-6 3z"/></svg>Training</span>
  <span><svg viewBox="0 0 24 24"><path d="M11 2h2l1 8 8 5v2l-8-2-1 5 3 2v1l-4-1-4 1v-1l3-2-1-5-8 2v-2l8-5z"/></svg>Travel</span>
</nav>

<section class="hero">
  <div class="photo" role="img" aria-label="A happy dog standing in front of blue ocean water"></div>
  <div class="inner">
    <h1>Save Big on Everything Your Dog Loves</h1>
    <p>Verified Deals Updated Daily</p>
    <div class="bar">Search for deals, brands, or categories<b>Search</b></div>
    <div class="chips"><span>Kibblo</span><span>PupPantry</span><span>Maple Hound</span></div>
  </div>
</section>

<section class="deals">
  <div class="wrap">
    <h2 class="section-title">Today's Top Deals</h2>
    <div class="deal-grid">
      <article class="deal">
        <div class="store"><i></i>Store1</div>
        <svg class="heart" viewBox="0 0 24 24" fill="none" stroke="#9ca3af" stroke-width="2"><path d="M12 21l-8.5-8.5a5 5 0 017-7L12 7l1.5-1.5a5 5 0 017 7z"/></svg>
        <span class="off">50% OFF</span>
        <p>Get 50% off on all premium dog food brands this weekend</p>
        <div class="exp"><svg width="12" height="12" viewBox="0 0 24 24" fill="none" stroke="#6b7280" stroke-width="2"><circle cx="12" cy="12" r="9"/><path d="M12 7v5l3 2"/></svg>Expires in 5 days</div>
        <div class="copy">Copy Code</div>
        <div class="ver"><svg width="13" height="13" viewBox="0 0 24 24"><circle cx="12" cy="12" r="11" fill="#10b981"/><path d="M7 12l3 3 6-6" stroke="#fff" stroke-width="3" fill="none"/></svg>Verified Deal</div>
      </article>
      <article class="deal">
        <div class="store"><i></i>Store2</div>
        <svg class="heart" viewBox="0 0 24 24" fill="none" stroke="#9ca3af" stroke-width="2"><path d="M12 21l-8.5-8.5a5 5 0 017-7L12 7l1.5-1.5a5 5 0 017 7z"/></svg>
        <span class="off">50% OFF</span>
        <p>Get 50% off on all premium dog food brands this weekend</p>
        <div class="exp"><svg width="12" height="12" viewBox="0 0 24 24" fill="none" stroke="#6b7280" stroke-width="2"><circle cx="12" cy="12" r="9"/><path d="M12 7v5l3 2"/></svg>Expires in 5 days</div>
        <div class="copy">Copy Code</div>
        <div class="ver"><svg width="13" height="13" viewBox="0 0 24 24"><circle cx="12" cy="12" r="11" fill="#10b981"/><path d="M7 12l3 3 6-6" stroke="#fff" stroke-width="3" fill="none"/></svg>Verified Deal</div>
      </article>
      <article class="deal">
        <div class="store"><i></i>Store3</div>
        <svg class="heart" viewBox="0 0 24 24" fill="none" stroke="#9ca3af" stroke-width="2"><path d="M12 21l-8.5-8.5a5 5 0 017-7L12 7l1.5-1.5a5 5 0 017 7z"/></svg>
        <span class="off">50% OFF</span>
        <p>Get 50% off on all premium dog food brands this weekend</p>
        <div class="exp"><svg width="12" height="12" viewBox="0 0 24 24" fill="none" stroke="#6b7280" stroke-width="2"><circle cx="12" cy="12" r="9"/><path d="M12 7v5l3 2"/></svg>Expires in 5 days</div>
        <div class="copy">Copy Code</div>
        <div class="ver"><svg width="13" height="13" viewBox="0 0 24 24"><circle cx="12" cy="12" r="11" fill="#10b981"/><path d="M7 12l3 3 6-6" stroke="#fff" stroke-width="3" fill="none"/></svg>Verified Deal</div>
      </article>
    </div>
  </div>
</section>

<section class="cats">
  <div class="wrap">
    <h2 class="section-title">Popular Categories</h2>
    <div class="cat-grid">
      <div class="cat" role="img" aria-label="Bags of dog food with scattered kibble" style="background:linear-gradient(135deg,#c0392b,#3f8f4a 50%,#d4a44a)"><svg viewBox="0 0 24 24"><circle cx="12" cy="15" r="6"/><circle cx="5" cy="8" r="2.5"/><circle cx="19" cy="8" r="2.5"/><circle cx="9" cy="4" r="2.5"/><circle cx="15" cy="4" r="2.5"/></svg><b>Dog Food</b><small>234 deals</small></div>
      <div class="cat" role="img" aria-label="Packages of dog treats" style="background:linear-gradient(135deg,#7a2a2a,#3a7a5a 50%,#c86a4a)"><svg viewBox="0 0 24 24"><path d="M2 2h10l10 10-10 10L2 12z"/></svg><b>Treats</b><small>156 deals</small></div>
      <div class="cat" role="img" aria-label="A pile of colourful dog toys" style="background:linear-gradient(135deg,#4f9a6a,#e0823a 50%,#3a8ec8)"><svg viewBox="0 0 24 24"><path d="M4 7h16v15H4z"/><path d="M8 7a4 4 0 018 0" fill="none" stroke="#fff" stroke-width="2"/></svg><b>Toys</b><small>189 deals</small></div>
      <div class="cat" role="img" aria-label="Dog health supplement bottles" style="background:linear-gradient(135deg,#b99a6a,#4a6a9a 55%,#d8c89a)"><svg viewBox="0 0 24 24"><path d="M12 2l9 4v6c0 5-4 9-9 10-5-1-9-5-9-10V6z"/></svg><b>Health</b><small>145 deals</small></div>
      <div class="cat" role="img" aria-label="Dog grooming bottles and brushes" style="background:linear-gradient(135deg,#a9a49c,#e0a050 40%,#7c7870)"><svg viewBox="0 0 24 24"><path d="M12 2c4 6 6 9 6 12a6 6 0 01-12 0c0-3 2-6 6-12z"/></svg><b>Grooming</b><small>98 deals</small></div>
      <div class="cat" role="img" aria-label="Training treats, clicker and a pouch" style="background:linear-gradient(135deg,#c8c2b8,#a87a4a 45%,#2e3440)"><svg viewBox="0 0 24 24"><path d="M12 4l11 5-11 5L1 9z"/><path d="M6 12v5c3 3 9 3 12 0v-5l-6 3z"/></svg><b>Training</b><small>123 deals</small></div>
    </div>
  </div>
</section>

<section class="stores">
  <div class="wrap">
    <h2 class="section-title">Featured Stores</h2>
    <div class="store-row"><div>Store1</div><div>Store2</div><div>Store3</div><div>Store4</div><div>Store5</div></div>
  </div>
</section>

<section class="tips">
  <div class="wrap">
    <h2 class="section-title">Pet Care Tips &amp; Advice</h2>
    <div class="tip-grid">
      <article class="tip"><div class="img" role="img" aria-label="Two small dogs running on a dirt path" style="background:linear-gradient(135deg,#8a6a4a,#c8a27a 50%,#6e5a40)"></div><div class="body"><div class="tag">Dog Care</div><h3>Essential Tips for Your Dog's Health and Wellness</h3><p>Learn the best practices for keeping your furry friend healthy and happy...</p><div class="read"><svg width="12" height="12" viewBox="0 0 24 24" fill="none" stroke="#6b7280" stroke-width="2"><circle cx="12" cy="12" r="9"/><path d="M12 7v5l3 2"/></svg>5 min read</div></div></article>
      <article class="tip"><div class="img" role="img" aria-label="A dog running across green grass" style="background:linear-gradient(135deg,#3f7a2a,#6aa83a 50%,#2e5a22)"></div><div class="body"><div class="tag">Dog Care</div><h3>Essential Tips for Your Dog's Health and Wellness</h3><p>Learn the best practices for keeping your furry friend healthy and happy...</p><div class="read"><svg width="12" height="12" viewBox="0 0 24 24" fill="none" stroke="#6b7280" stroke-width="2"><circle cx="12" cy="12" r="9"/><path d="M12 7v5l3 2"/></svg>5 min read</div></div></article>
      <article class="tip"><div class="img" role="img" aria-label="A veterinarian examining a dog in a clinic" style="background:linear-gradient(135deg,#b8c4d0,#c8884a 45%,#e8ecf0)"></div><div class="body"><div class="tag">Dog Care</div><h3>Essential Tips for Your Dog's Health and Wellness</h3><p>Learn the best practices for keeping your furry friend healthy and happy...</p><div class="read"><svg width="12" height="12" viewBox="0 0 24 24" fill="none" stroke="#6b7280" stroke-width="2"><circle cx="12" cy="12" r="9"/><path d="M12 7v5l3 2"/></svg>5 min read</div></div></article>
    </div>
  </div>
</section>

<section class="trust">
  <div><span class="ic"><svg width="26" height="26" viewBox="0 0 24 24"><circle cx="12" cy="12" r="11" fill="#3b82f6"/><path d="M7 12l3 3 6-6" stroke="#fff" stroke-width="2.5" fill="none"/></svg></span><h4>100% Verified Deals</h4><p>All deals are manually verified</p></div>
  <div><span class="ic"><svg width="26" height="26" viewBox="0 0 24 24"><circle cx="12" cy="12" r="11" fill="#3b82f6"/><path d="M7 12l3 3 6-6" stroke="#fff" stroke-width="2.5" fill="none"/></svg></span><h4>Daily Updates</h4><p>New deals added every day</p></div>
  <div><span class="ic"><svg width="26" height="26" viewBox="0 0 24 24"><circle cx="12" cy="12" r="11" fill="#3b82f6"/><path d="M7 12l3 3 6-6" stroke="#fff" stroke-width="2.5" fill="none"/></svg></span><h4>500+ Partner Stores</h4><p>Top pet stores and brands</p></div>
  <div><span class="ic"><svg width="26" height="26" viewBox="0 0 24 24"><circle cx="12" cy="12" r="11" fill="#3b82f6"/><path d="M7 12l3 3 6-6" stroke="#fff" stroke-width="2.5" fill="none"/></svg></span><h4>Community Tested</h4><p>Trusted by pet parents</p></div>
</section>

<section class="news">
  <h2>Never Miss a Deal</h2>
  <p>Get the best pet deals delivered to your inbox</p>
  <form><div class="in">Enter your email</div><div class="btn">Subscribe</div></form>
</section>

<footer class="footer">
  <div class="wrap">
    <div class="foot-cols">
      <div><div class="foot-brand"><i></i>TailMart</div><p>Your trusted source for the best pet deals and discounts.</p></div>
      <div><h5>Quick Links</h5><ul><li>About Us</li><li>Contact</li><li>Blog</li><li>FAQs</li></ul></div>
      <div><h5>Categories</h5><ul><li>Dog Food</li><li>Toys</li><li>Health</li><li>Services</li></ul></div>
      <div><h5>Help &amp; Support</h5><ul><li>Terms of Service</li><li>Privacy Policy</li><li>Cookie Policy</li></ul></div>
    </div>
    <div class="foot-bottom"><span>© 2024 TailMart. All rights reserved.</span><div class="social"><span aria-label="Social link"></span><span aria-label="Social link"></span><span aria-label="Social link"></span><span aria-label="Social link"></span></div></div>
  </div>
</footer>

</body>
</html>
```